Simple scorekeeping for soccer moms & football fathers

... and volleyball, and baseball, ... We are working on an app that allows parents to very easily keep track of significant events in their children's sports lives & share that with friends & family.

We need graphic designs, colors, and (if possible) interaction design for the iOS 7 version of the application. The design must evoke the joy of seeing your child's home run, goal, or spike, while remaining simple to use so as not to take away from the experience of the game itself. The app is intended to *enhance* the child's and parents' experiences with things like video, photo, scores, chats, and history.

The new app design needs to evoke the fun we all remember from little league, and be more "modern" to fit with current IOS7 aesthetics. The splash screen of the current app is attached for inspiration. We would like to stick with this type of theme, but with a modern iOS7 design for a smooth transition.
Updates

Project Deadline Extended
Reason: A number of people only accepted the contest yesterday & I want to give them time. Also, I need to post a more thorough walkthrough of the app for those who haven't seen it yet.

There was a request for a walkthrough of the current app.  I put together a ppt with each view and a brief description of what they are responsible for, at this link on dropbox: https://www.filecrate-demo.net/s/qmw47trbzpl2vx/TallyNest-app 

I hope this helps to illuminate some of what I'm after.

Project Deadline Extended
Reason: There has only been 1 design submitted. Let's extend the time & get more designs. Please let me know what else you need.

Hello all!  I've reposted the walkthrough directly to the brief.  This is a PDF slideshow with descriptions of the existing screens on the app.  It's not 100% that you have to have this as your design, but rather just there to give you a sense for the feel of the app how it is today & hopefully to inspire your designs.

Target Market(s)

Parents of little league-age children. The parents are typically in their 30's, middle-income, and college educated. The children are between 5-12. All the participants are english-speaking, United States residents, most likely in the midwest & south.

Industry/Entity Type

Events

Font styles to use
Sans Serif

Colors

Designer to choose colors to be used in the design.

Requirements
Must have
• Youth feel. centered around the child. Must deliver png's, adobe illustrator files, all sized for iOS7 and the iPhone 4 and 5s. Must fit with new IOS7 design guidelines.
Nice to have
• Items that evoke the feeling of little league and children playing games like baseball, soccer, football, hockey, lacrosse...
Should not have
• anything adult-specific.

```html
<!DOCTYPE html>
<html lang="en">
<head>
<meta charset="utf-8">
<title>PlayDay – Log in</title>
<link rel="stylesheet" href="https://fonts.googleapis.com/css2?family=Open+Sans:wght@300;400;600;700;800&display=swap">
<style>
  :root {
    --sky-top: #4fb8ef;
    --sky-mid: #6cc8f5;
    --sky-low: #8ed6f7;
    --status-bg: #3b3d40;
    --status-text: #d8d8d8;
    --white: #ffffff;
    --field-bg: rgba(40, 140, 200, 0.45);
    --field-edge: rgba(255, 255, 255, 0.35);
    --social-text: #2f9ad8;
    --social-mark: #2f9ad8;
    --signup: #86d66a;
    --signup-edge: #6cbf52;
    --grass: #6cc04a;
    --grass-dark: #4f9c35;
  }
  * { box-sizing: border-box; margin: 0; padding: 0; }
  html, body { width: 820px; height: 1200px; overflow: hidden; }
  body {
    font-family: "Open Sans", Arial, sans-serif;
    background: var(--sky-top);
  }
  .screen {
    position: relative;
    width: 820px;
    height: 1200px;
    background: linear-gradient(180deg, var(--sky-top) 0%, var(--sky-mid) 40%, var(--sky-low) 70%, var(--sky-mid) 100%);
    overflow: hidden;
  }
  .status-bar {
    position: absolute; top: 0; left: 0; right: 0;
    height: 36px;
    background: var(--status-bg);
    color: var(--status-text);
    font-weight: 600; font-size: 24px;
    display: flex; align-items: center; justify-content: space-between;
    padding: 0 14px;
  }
  .status-bar .carrier, .status-bar .battery { display: flex; align-items: center; gap: 8px; }
  .brand {
    position: absolute; top: 96px; left: 0; right: 0;
    text-align: center; color: var(--white);
  }
  .brand-name { font-weight: 800; font-size: 82px; line-height: 1; letter-spacing: 1px; }
  .tagline { margin-top: 18px; font-size: 19px; font-weight: 400; letter-spacing: 3px; }
  .login-form {
    position: absolute; top: 292px; left: 170px; width: 480px;
  }
  .field {
    display: block; width: 100%; height: 56px;
    background: var(--field-bg);
    border: 1px solid var(--field-edge);
    color: var(--white);
    font: 300 24px "Open Sans", Arial, sans-serif;
    text-align: center; line-height: 54px;
    margin-bottom: 42px;
  }
  .alt-login {
    text-align: center; color: var(--white);
    font-weight: 600; font-size: 18px;
    margin-top: 14px;
  }
  .social-row {
    display: flex; justify-content: space-between; margin-top: 44px;
  }
  .social-btn {
    width: 220px; height: 52px;
    background: var(--white);
    border-radius: 2px;
    display: flex; align-items: center; justify-content: center; gap: 18px;
    color: var(--social-text); font-size: 21px; font-weight: 400;
  }
  .social-btn .mark { width: 34px; height: 34px; background: var(--social-mark); border-radius: 3px; }
  .signup-btn {
    display: block; width: 100%; height: 58px; margin-top: 72px;
    background: var(--signup);
    border-bottom: 3px solid var(--signup-edge);
    color: var(--white); font-weight: 700; font-size: 28px;
    text-align: center; line-height: 56px;
  }
  .hero-art {
    position: absolute; left: 0; right: 0; bottom: 0; height: 380px;
    background: linear-gradient(180deg, rgba(142,214,247,0) 0%, var(--sky-low) 45%, var(--grass) 72%, var(--grass-dark) 100%);
  }
</style>
</head>
<body>
  <main class="screen">
    <div class="status-bar">
      <span class="carrier">
        <svg width="40" height="20" viewBox="0 0 40 20" aria-hidden="true">
          <rect x="0" y="14" width="5" height="6" fill="#d8d8d8"/>
          <rect x="8" y="11" width="5" height="9" fill="#d8d8d8"/>
          <rect x="16" y="8" width="5" height="12" fill="#d8d8d8"/>
          <rect x="24" y="4" width="5" height="16" fill="#d8d8d8"/>
          <rect x="32" y="0" width="5" height="20" fill="#d8d8d8"/>
        </svg>
        CELLO
      </span>
      <span class="time">10:35 AM</span>
      <span class="battery">
        <svg width="22" height="22" viewBox="0 0 22 22" aria-hidden="true">
          <circle cx="11" cy="11" r="10" fill="#d8d8d8"/>
          <path d="M11 4 V11 H16" stroke="#3b3d40" stroke-width="2.5" fill="none"/>
        </svg>
        65%
        <svg width="44" height="22" viewBox="0 0 44 22" aria-hidden="true">
          <rect x="1" y="2" width="38" height="18" rx="2" fill="none" stroke="#d8d8d8" stroke-width="2"/>
          <rect x="4" y="5" width="22" height="12" fill="#d8d8d8"/>
          <rect x="40" y="8" width="3" height="6" fill="#d8d8d8"/>
        </svg>
      </span>
    </div>

    <header class="brand">
      <h1 class="brand-name">PLAYDAY</h1>
      <p class="tagline">Fun &amp; Easy way to keep scores</p>
    </header>

    <section class="login-form">
      <div class="field">Email Address</div>
      <div class="field">Password</div>
      <p class="alt-login">Or Log in using</p>
      <div class="social-row">
        <div class="social-btn"><span class="mark"></span>Friendly</div>
        <div class="social-btn"><span class="mark"></span>Chirpy</div>
      </div>
      <div class="signup-btn">SIGN UP</div>
    </section>

    <div class="hero-art" role="img" aria-label="Cartoon child baseball batter in pinstripe uniform standing on a green hill under soft clouds"></div>
  </main>
</body>
</html>
```